Billboard For Marcus Delvane

Need a Billboard 8ft. High x 16ft. Long. Ive attached a former billboard and looking for the same thing just updated with:
Wardens Guild Award Logo - 2020, 2022
Summit Lantern award Logo - 2022

Thanks.

```html
<!DOCTYPE html>
<html lang="en">
<head>
<meta charset="utf-8">
<title>Billboard – Marcus Delvane</title>
<link rel="stylesheet" href="https://fonts.googleapis.com/css2?family=Jost:ital,wght@0,400;0,500;0,600;0,700;0,800;1,700&display=swap">
<style>
  :root {
    --ink: #111111;
    --paper: #ffffff;
    --band: #0d0d0d;
    --accent: #e3262b;
    --stage: #e8ecf1;
    --muted: #3a3a3a;
    --photo-top: #8fa4bf;
    --photo-bottom: #2e4f86;
  }
  * { box-sizing: border-box; margin: 0; padding: 0; }
  html, body {
    width: 1200px; height: 800px; overflow: hidden;
    background: var(--stage);
    font-family: "Jost", "Futura", sans-serif;
  }
  .billboard {
    position: absolute; left: 40px; top: 120px;
    width: 1120px; height: 560px;
    background: var(--paper);
    overflow: hidden;
    box-shadow: 0 6px 24px rgba(0,0,0,.18);
  }
  .billboard p, .billboard h1 { white-space: nowrap; }
  .agent-photo {
    position: absolute; left: 0; top: 0;
    width: 340px; height: 250px;
    background: linear-gradient(180deg, var(--photo-top) 0%, var(--photo-bottom) 100%);
  }
  .headline {
    position: absolute; left: 372px; top: 40px;
    font-weight: 800; color: var(--ink);
    font-size: 80px; line-height: 1; letter-spacing: 1px;
    text-transform: uppercase;
  }
  .headline .call { color: var(--accent); margin-left: 14px; }
  .info-band {
    position: absolute; left: 0; top: 250px;
    width: 1120px; height: 130px;
    background: var(--band);
  }
  .agent-name {
    position: absolute; left: 36px; top: 274px;
    color: var(--paper); font-weight: 700; font-size: 42px; line-height: 1;
    letter-spacing: 1px; text-transform: uppercase;
  }
  .agent-title {
    position: absolute; left: 40px; top: 326px;
    color: var(--paper); font-weight: 500; font-size: 15px;
    letter-spacing: 5px; text-transform: uppercase;
  }
  .band-divider {
    position: absolute; left: 470px; top: 275px;
    width: 2px; height: 80px; background: var(--paper);
  }
  .phone {
    position: absolute; left: 500px; top: 272px;
    color: var(--paper); font-weight: 600; font-size: 78px; line-height: 1;
    letter-spacing: 1px;
  }
  .award {
    position: absolute; top: 426px;
    display: flex; align-items: center; gap: 14px;
    color: var(--ink);
  }
  .award--guild { left: 30px; }
  .award--lantern { left: 340px; }
  .award-seal {
    width: 76px; height: 76px; border-radius: 50%;
    border: 3px solid var(--ink); flex: none;
  }
  .award--lantern .award-seal { width: 48px; height: 48px; background: var(--ink); border: none; }
  .award-text { font-weight: 500; line-height: 1; text-transform: uppercase; }
  .award-brand { font-size: 10px; letter-spacing: 1px; }
  .award-name { font-size: 24px; margin-top: 3px; }
  .award-meta { font-size: 10px; margin-top: 5px; letter-spacing: 1px; }
  .social {
    position: absolute; left: 624px; top: 452px;
    padding-left: 12px; border-left: 2px solid var(--muted);
    font-weight: 600; font-size: 15px; line-height: 24px; color: var(--accent);
  }
  .tagline {
    position: absolute; left: 800px; top: 410px;
    width: 320px; height: 110px;
    background: var(--accent);
    display: flex; align-items: center; justify-content: center;
    color: var(--paper); font-style: italic; font-weight: 700;
    font-size: 24px; line-height: 1.15; text-align: center;
    text-transform: uppercase;
  }
</style>
</head>
<body>
  <main class="billboard">
    <div class="agent-photo" role="img" aria-label="Portrait photo of Marcus Delvane in a blue shirt and tie"></div>

    <h1 class="headline">Buying or<br>Selling?<span class="call">Call</span></h1>

    <div class="info-band"></div>
    <p class="agent-name">Marcus Delvane</p>
    <p class="agent-title">Sales Representative</p>
    <span class="band-divider"></span>
    <p class="phone">613.555.0142</p>

    <div class="award award--guild">
      <span class="award-seal"></span>
      <div class="award-text">
        <p class="award-brand">Harbourline Realty</p>
        <p class="award-name">Wardens Guild</p>
        <p class="award-meta">National Top 1% | 2020 | 2022</p>
      </div>
    </div>

    <div class="award award--lantern">
      <span class="award-seal"></span>
      <div class="award-text">
        <p class="award-brand">Harbourline Realty</p>
        <p class="award-name">Summit Lantern</p>
        <p class="award-name">Award 2022</p>
      </div>
    </div>

    <p class="social">@mdelvanehomes</p>

    <p class="tagline">Focused, driven,<br>and experienced!</p>
  </main>
</body>
</html>
```